Want to go online this week, rush project, everything is there, just make it pretty

I need a pretty html5/css template for a already made site. Please do not rearrange anything unless you feel you can simplify the design. I have a raw site. Please play with the site by making an account with coupon code PLUMWALKERS for free signup. Log in, log out, download as many designs as you can, then log in and log out. See everything cause it's brand new and I need it neat and pretty over the next few days if not sooner. So, after all that, the site is http://StitchloomPatternHub.example
Updates

Is anyone working on something to submit? If you have something please submit asap as I will be closing this Sat night or Sunday morning

Industry/Entity Type

Online

Coding

Coded - Design and coding required

```html
<!DOCTYPE html>
<html lang="en">
<head>
<meta charset="utf-8">
<title>StitchloomPatternHub.example</title>
<link href="https://fonts.googleapis.com/css2?family=Fira+Sans+Extra+Condensed:wght@400;500;600;700&family=Great+Vibes&display=swap" rel="stylesheet">
<style>
  :root {
    --top-bar: #ececec;
    --ink: #111111;
    --grey-text: #6d6d6d;
    --label-grey: #777777;
    --pink: #ee7fb6;
    --logo-pink: #e86aa8;
    --blue-top: #2b93d1;
    --blue-bottom: #0d5f9c;
    --magenta-top: #c6338a;
    --magenta-bottom: #9d1c5b;
    --green-top: #4d7e36;
    --green-bottom: #2b4c1d;
    --white: #ffffff;
  }
  * { margin: 0; padding: 0; box-sizing: border-box; }
  html, body { width: 1200px; height: 813px; overflow: hidden; background: var(--white); }
  body { position: relative; font-family: "Fira Sans Extra Condensed", "Arial Narrow", sans-serif; color: var(--ink); }

  .top-bar { position: absolute; left: 0; top: 0; width: 1200px; height: 51px; background: var(--top-bar); }
  .logo-arch { position: absolute; left: 106px; top: -30px; width: 360px; height: 200px; background: var(--white); border-radius: 50% 50% 0 0 / 60% 60% 0 0; }

  .brand { position: absolute; left: 150px; top: 76px; width: 270px; display: flex; align-items: center; gap: 8px; }
  .brand-dot { width: 14px; height: 14px; border-radius: 50%; background: var(--logo-pink); flex: none; }
  .brand-name { font-size: 21px; font-weight: 500; color: var(--logo-pink); white-space: nowrap; }

  .main-nav { position: absolute; right: 299px; top: 19px; font-size: 13px; letter-spacing: -0.2px; color: var(--ink); white-space: nowrap; }
  .main-nav a { color: var(--ink); text-decoration: none; }
  .main-nav .current { font-weight: 600; }
  .main-nav .sep { margin: 0 2px; }

  .btn { position: absolute; display: flex; align-items: center; justify-content: space-between; color: var(--white); font-weight: 600; text-transform: uppercase; text-decoration: none; white-space: nowrap; border-radius: 4px; border: 1px solid rgba(0,0,0,.45); box-shadow: 0 1px 2px rgba(0,0,0,.25); }
  .btn-signup { left: 932px; top: 9px; width: 118px; height: 31px; padding: 0 18px 0 25px; font-size: 17px; background: linear-gradient(var(--blue-top), var(--blue-bottom)); }
  .btn-register { left: 506px; top: 473px; width: 213px; height: 60px; padding: 0 22px 0 34px; font-size: 22px; background: linear-gradient(var(--magenta-top), var(--magenta-bottom)); }
  .btn-preorder { left: 782px; top: 679px; width: 231px; height: 60px; padding: 0 26px 0 34px; font-size: 22px; background: linear-gradient(var(--green-top), var(--green-bottom)); }

  .stat { position: absolute; top: 74px; text-align: center; }
  .stat-designs { left: 672px; width: 178px; }
  .stat-sets { left: 868px; width: 164px; }
  .stat-number { font-size: 62px; font-weight: 400; color: var(--pink); line-height: 1; letter-spacing: 1px; }
  .stat-label { margin-top: 10px; font-size: 14px; color: var(--label-grey); display: flex; align-items: center; justify-content: center; gap: 10px; white-space: nowrap; }
  .stat-label::before, .stat-label::after { content: ""; width: 19px; height: 1px; background: var(--label-grey); }

  .hero { position: absolute; left: 0; top: 188px; width: 1200px; height: 410px; overflow: hidden; }
  .hero-photo { position: absolute; inset: 0;
    background:
      radial-gradient(ellipse 300px 230px at 600px 230px, #ffffff 55%, rgba(255,255,255,0) 100%),
      linear-gradient(90deg, #7a5a22 0%, #a86b2a 12%, #d49a3a 22%, #c9b27a 32%, #f2ece0 42%, #ffffff 50%, #eef3f6 58%, #8fb8d2 68%, #5f8fb6 76%, #b05aa8 86%, #7a4aa0 100%);
  }
  .hero-copy { position: absolute; left: 0; top: 146px; width: 1200px; text-align: center; }
  .hero-title { font-size: 41px; font-weight: 600; color: var(--grey-text); line-height: 38px; letter-spacing: -0.5px; }
  .hero-sub { margin-top: 14px; font-size: 19px; font-weight: 400; color: var(--grey-text); }

  .dvd-offer { position: absolute; left: 157px; top: 680px; }
  .dvd-title { font-size: 44px; font-weight: 600; color: var(--ink); line-height: 1; white-space: nowrap; letter-spacing: -0.5px; }
  .dvd-soon { position: absolute; left: 274px; top: 44px; font-family: "Great Vibes", cursive; font-size: 24px; color: var(--logo-pink); white-space: nowrap; }
  .dvd-product { position: absolute; left: 582px; top: 642px; width: 138px; height: 131px; border-radius: 6px; background: linear-gradient(135deg, #ffffff 0%, #e4e4e4 60%, #bdbdbd 100%); }
</style>
</head>
<body>
  <div class="top-bar"></div>
  <div class="logo-arch"></div>

  <div class="brand">
    <span class="brand-dot"></span>
    <span class="brand-name">StitchloomPatternHub.example</span>
  </div>

  <nav class="main-nav">
    <a class="current" href="#">Home</a><span class="sep">|</span><a href="#">Register</a><span class="sep">|</span><a href="#">Account</a><span class="sep">|</span><a href="#">Contact</a><span class="sep">|</span><a href="#">Search</a><span class="sep">|</span><a href="#">Bookmark This Page</a>
  </nav>

  <a class="btn btn-signup" href="#">Sign up
    <svg width="12" height="14" viewBox="0 0 12 14" aria-hidden="true"><path d="M1 1h10v6c0 3-2.5 5-5 6-2.5-1-5-3-5-6z" fill="none" stroke="#fff" stroke-width="2"/><path d="M6 2v10" stroke="#fff" stroke-width="2"/></svg>
  </a>

  <div class="stat stat-designs">
    <div class="stat-number">27,906</div>
    <div class="stat-label">unique designs online</div>
  </div>
  <div class="stat stat-sets">
    <div class="stat-number">1,982</div>
    <div class="stat-label">design sets/packs</div>
  </div>

  <section class="hero">
    <div class="hero-photo" role="img" aria-label="Skeins of embroidery thread in warm browns and golds on the left and blues, greys and purples on the right, framing a white centre"></div>
    <div class="hero-copy">
      <h1 class="hero-title">Thousands of machine ready<br>embroidery designs</h1>
      <p class="hero-sub">Lorem Ipsum Consectetur Adipiscing Elit</p>
    </div>
  </section>

  <a class="btn btn-register" href="#">Register now
    <svg width="24" height="22" viewBox="0 0 24 22" aria-hidden="true"><path d="M15 3H3v17h16v-8" fill="none" stroke="#fff" stroke-width="2"/><path d="M9 14l1-4 9-9 3 3-9 9z" fill="none" stroke="#fff" stroke-width="2" stroke-linejoin="round"/></svg>
  </a>

  <div class="dvd-offer">
    <div class="dvd-title">Get all designs on DVD</div>
    <div class="dvd-soon">Coming soon!</div>
  </div>
  <div class="dvd-product" role="img" aria-label="White DVD case with a disc in front"></div>

  <a class="btn btn-preorder" href="#">Pre-order now
    <svg width="26" height="20" viewBox="0 0 26 20" aria-hidden="true"><rect x="1" y="1" width="24" height="18" rx="2" fill="none" stroke="#fff" stroke-width="2"/><rect x="1" y="5" width="24" height="4" fill="#fff"/><rect x="4" y="13" width="6" height="2" fill="#fff"/><rect x="12" y="13" width="4" height="2" fill="#fff"/></svg>
  </a>
</body>
</html>
```